Sleek wordpress site for Brightwell finishing systems

We are a commercial job shop that serves B2B, govt & LEO and retail clients.We need a wordpress site with 6 individual pages: homepage, coating, laser engraving, laser cutting, part marking, and contact us. I have attached an outline of the desired flow and sub headings for each page. I would like to incorporate the colors of the logo through out the site to be clean and sleek enough to appeal to B2B commercial clients yet be inviting enough for retail clients.

I would like to have easy picture functionality so photographs on each page can be updated easily.

Target Market(s)

B2B industrial & Govt and Military part marking, laser engraving and coating: machine shops, aerospace companies, tool manufactures. Retail: personalized gifts, Job Shop

Coding

Coded - Design and coding required

Font styles to use
Sans Serif
Other font styles liked:
• Open to suggestion

Colors
0255a3
3176b5
eaf1f7
cfdeed
ffffff

Requirements
Must have
• Clean easy to navigate flow, separate pages as indicated on attached outline, high class feel. Great picture functionality, professional and inviting feel,
• **update: needs to be optimized for mobile, should have a gallery function. Gallery can be an additional page or embedded
Nice to have
• Social media connectivity links,
Should not have
• crappy plugins that make back-end management difficult, no blog

```html
<!DOCTYPE html>
<html lang="en">
<head>
<meta charset="utf-8">
<title>Brightwell Finishing Systems</title>
<link href="https://fonts.googleapis.com/css2?family=Jost:wght@400;500;600&family=Tinos:wght@700&family=Orbitron:wght@700&family=Lato:ital,wght@1,700&family=Poppins:wght@400;500&display=swap" rel="stylesheet">
<style>
:root{
  --brand:#0255a3;
  --brand-2:#3176b5;
  --brand-dark:#024a8f;
  --tint:#eaf1f7;
  --tint-2:#cfdeed;
  --white:#ffffff;
  --page:#f4f4f4;
  --ink:#333333;
  --muted:#6b6b6b;
  --rule:#c9c9c9;
}
*{box-sizing:border-box;margin:0;padding:0}
html,body{width:1200px;height:2236px;overflow:hidden}
body{background:var(--page);font-family:"Poppins",sans-serif;color:var(--ink);position:relative}
.abs{position:absolute}
.sheet{left:67px;top:15px;width:1066px;height:2202px;background:var(--white)}

/* header */
.brand{left:86px;top:52px;display:flex;align-items:center;gap:12px;font-family:"Jost",sans-serif;font-weight:600;font-size:22px;color:var(--brand)}
.brand-dot{width:34px;height:34px;border-radius:50%;background:var(--brand)}
.contact-item{top:64px;display:flex;align-items:center;font-family:"Jost",sans-serif;font-size:17px;color:#333}
.contact-item .sep{width:1px;height:40px;background:#ddd;margin:0 12px}

/* nav */
.nav{left:67px;top:156px;width:1066px;height:63px;background:linear-gradient(#0a5cae,var(--brand))}
.nav-link{top:0;height:63px;line-height:63px;font-family:"Jost",sans-serif;font-size:18px;color:var(--white)}
.nav-home{left:77px;top:156px;width:124px;height:63px;background:var(--brand-2);line-height:63px;text-align:center;font-family:"Jost",sans-serif;font-weight:600;font-size:19px;color:var(--white)}
.search{left:913px;top:173px;width:178px;height:30px;background:var(--white);font-family:"Lato",sans-serif;font-style:italic;font-size:12px;color:#777;padding:8px 12px}
.search-btn{left:1091px;top:173px;width:31px;height:30px;background:#2a2a2a;display:flex;align-items:center;justify-content:center}

/* hero */
.hero{left:77px;top:228px;width:1045px;height:574px;background:radial-gradient(ellipse at 68% 60%,#f0a35a 0%,#8b4a8c 22%,#3a3a86 48%,#1c2350 80%)}
.hero-title{left:122px;top:362px;font-family:"Orbitron",sans-serif;font-weight:700;font-size:43px;line-height:58px;color:var(--white);letter-spacing:1px;text-shadow:2px 2px 4px rgba(0,0,0,.5)}
.hero-text{left:122px;top:490px;width:600px;font-family:"Lato",sans-serif;font-style:italic;font-weight:700;font-size:16px;line-height:26px;color:var(--white)}
.btn{font-family:"Jost",sans-serif;font-size:19px;text-align:center;border-radius:3px}
.btn-primary{background:linear-gradient(var(--brand-2),var(--brand));color:var(--white)}
.btn-light{background:var(--white);color:var(--brand)}
.dots{left:561px;top:829px;display:flex;gap:7px}
.dots span{width:14px;height:14px;border-radius:50%;background:#ccc}
.dots span:first-child{background:var(--brand)}

/* sections */
.section-title{font-family:"Tinos",serif;font-weight:700;font-size:34px;color:var(--brand)}
.rule{height:1px;background:var(--rule)}
.service-img{top:968px;width:240px;height:157px;box-shadow:0 8px 8px -4px rgba(0,0,0,.3)}
.service-name{top:1152px;width:240px;text-align:center;font-family:"Jost",sans-serif;font-weight:500;font-size:24px;color:var(--brand)}
.service-text{top:1195px;width:240px;text-align:center;font-size:13.5px;line-height:25px;color:var(--muted)}
.service-btn{top:1286px;width:146px;height:52px;line-height:52px}

.about-name{left:77px;top:1540px;width:190px;display:flex;align-items:center;gap:10px;font-family:"Jost",sans-serif;font-weight:600;font-size:22px;line-height:28px;color:var(--brand)}
.about-name .brand-dot{flex:none;width:40px;height:40px}
.about-text{left:295px;top:1496px;width:440px;font-size:13.5px;line-height:24.5px;color:var(--muted)}
.video{left:77px;top:1709px;width:656px;height:186px;background:linear-gradient(100deg,#2a2420,#5a3a22 45%,#2b2a30)}
.play{left:379px;top:1777px;width:50px;height:50px;border:3px solid var(--white);border-radius:50%}

/* quote */
.quote{left:790px;top:1427px;width:332px;height:468px;background:var(--white);box-shadow:0 2px 8px rgba(0,0,0,.25)}
.quote-head{left:790px;top:1427px}
.quote-kicker{left:790px;top:1441px;width:332px;text-align:center;font-family:"Jost",sans-serif;font-weight:600;font-size:12px;color:var(--white)}
.quote-title{left:790px;top:1460px;width:332px;text-align:center;font-family:"Jost",sans-serif;font-weight:600;font-size:28px;color:var(--white)}
.field{left:811px;width:290px;height:45px;border:1px solid #dcdcdc;background:linear-gradient(#fff,#ececec);font-size:13px;color:#555;padding:13px 10px}
.send{left:811px;top:1818px;width:290px;height:46px;line-height:46px;font-size:17px}

/* footer */
.footer{left:67px;top:1970px;width:1066px;height:247px;background:var(--brand)}
.foot-home{left:77px;top:2000px;width:93px;height:41px;border:1px solid var(--white);border-radius:21px;line-height:39px;text-align:center;font-size:14px;color:var(--white)}
.foot-link{top:2011px;font-size:14px;color:var(--white)}
.foot-sep{top:2011px;font-size:14px;color:var(--tint-2)}
.social{top:2000px;width:42px;height:42px;border-radius:50%;border:1px solid var(--white)}
.social.filled{background:var(--white)}
.foot-rule{left:77px;top:2073px;width:1045px;height:1px;background:rgba(255,255,255,.35)}
.foot-icon{top:2114px;width:42px;height:42px;border-radius:50%;background:var(--white);display:flex;align-items:center;justify-content:center}
.foot-info{font-family:"Jost",sans-serif;font-size:17px;color:var(--white);line-height:25px}
.copy{left:867px;top:2113px;font-size:11.5px;line-height:21px;color:var(--white)}
.copy b{font-weight:500}
</style>
</head>
<body>
<div class="abs sheet"></div>

<header>
  <div class="abs brand"><span class="brand-dot"></span>Brightwell finishing systems</div>
  <div class="abs contact-item" style="left:680px">
    <svg width="30" height="36" viewBox="0 0 24 24"><path fill="#0255a3" d="M6.6 2.5l3 3.6-2 2.3c1.2 3 3.3 5.3 6.1 6.8l2.3-2 3.5 3.1-1.8 3.2C10.4 19.6 4.2 13 3.6 5.1z"/></svg>
    <span class="sep"></span>480.555.0182
  </div>
  <div class="abs contact-item" style="left:872px">
    <svg width="34" height="26" viewBox="0 0 34 26"><rect x="1" y="1" width="32" height="24" rx="2" fill="#0255a3"/><path d="M2 3l15 12L32 3M2 24l11-10M32 24L21 14" stroke="#fff" stroke-width="2" fill="none"/></svg>
    <span class="sep"></span>hello@brightwellfinishing.com
  </div>
</header>

<nav>
  <div class="abs nav"></div>
  <div class="abs nav-home">Home</div>
  <div class="abs nav-link" style="left:246px;top:156px">Coating</div>
  <div class="abs nav-link" style="left:349px;top:156px">Laser Engraving</div>
  <div class="abs nav-link" style="left:517px;top:156px">Lesar Cutting</div>
  <div class="abs nav-link" style="left:662px;top:156px">Part Marketing</div>
  <div class="abs nav-link" style="left:818px;top:156px">Contact</div>
  <div class="abs search">Search here.....</div>
  <div class="abs search-btn"><svg width="18" height="18" viewBox="0 0 18 18"><circle cx="7" cy="7" r="5.5" stroke="#fff" stroke-width="1.6" fill="none"/><path d="M11 11l5.5 5.5" stroke="#fff" stroke-width="1.8"/></svg></div>
</nav>

<section>
  <div class="abs hero" role="img" aria-label="Photo of a laser cutting head throwing sparks across a metal sheet"></div>
  <h1 class="abs hero-title">BRIGHTWELL FINISHING<br>SYSTEMS</h1>
  <p class="abs hero-text">Lorem Ipsum is simply dummy text of the printing and typesetting industry. Lorem Ipsum has been the industry's standard dummy text ever since the 1500s.</p>
  <div class="abs btn btn-primary" style="left:119px;top:568px;width:145px;height:56px;line-height:56px">READ MORE</div>
  <div class="abs btn btn-light" style="left:276px;top:568px;width:144px;height:56px;line-height:56px">CONTACT US</div>
  <div class="abs dots"><span></span><span></span><span></span><span></span></div>
</section>

<section>
  <div class="abs rule" style="left:403px;top:906px;width:74px"></div>
  <h2 class="abs section-title" style="left:497px;top:882px">Our Services</h2>
  <div class="abs rule" style="left:725px;top:906px;width:74px"></div>

  <div class="abs service-img" style="left:77px;background:linear-gradient(135deg,#5b6a78,#3d4852 60%,#6b4b3a)" role="img" aria-label="Photo of a worker torch-coating a metal pipe"></div>
  <div class="abs service-img" style="left:346px;background:linear-gradient(160deg,#3a3f45,#9aa0a6 55%,#c9a98a)" role="img" aria-label="Photo of a laser engraving bed with cut metal parts"></div>
  <div class="abs service-img" style="left:614px;background:linear-gradient(160deg,#2a2520,#7a5a3a 55%,#4a3a2c)" role="img" aria-label="Photo of a laser cutter with sparks over sheet metal"></div>
  <div class="abs service-img" style="left:882px;background:linear-gradient(160deg,#4a5248,#8a8a6a 50%,#3c4a4c)" role="img" aria-label="Photo of a laser marking head over a metal part"></div>

  <h3 class="abs service-name" style="left:77px">Coating</h3>
  <h3 class="abs service-name" style="left:346px">Laser Engraving</h3>
  <h3 class="abs service-name" style="left:614px">Lesar Cutting</h3>
  <h3 class="abs service-name" style="left:882px">Part Marketing</h3>

  <p class="abs service-text" style="left:77px">Lorem Ipsum is simply dummy text of the printing and typesetting industry.</p>
  <p class="abs service-text" style="left:346px">Lorem Ipsum is simply dummy text of the printing and typesetting industry.</p>
  <p class="abs service-text" style="left:614px">Lorem Ipsum is simply dummy text of the printing and typesetting industry.</p>
  <p class="abs service-text" style="left:882px">Lorem Ipsum is simply dummy text of the printing and typesetting industry.</p>

  <div class="abs btn btn-primary service-btn" style="left:124px">READ MORE</div>
  <div class="abs btn btn-primary service-btn" style="left:393px">READ MORE</div>
  <div class="abs btn btn-primary service-btn" style="left:661px">READ MORE</div>
  <div class="abs btn btn-primary service-btn" style="left:929px">READ MORE</div>
</section>

<section>
  <h2 class="abs section-title" style="left:80px;top:1424px">About Us</h2>
  <div class="abs rule" style="left:251px;top:1449px;width:73px"></div>
  <div class="abs about-name"><span class="brand-dot"></span>Brightwell finishing systems</div>
  <p class="abs about-text">Lorem Ipsum is simply dummy text of the printing and typesetting industry. Lorem Ipsum has been the industry's standard dummy text ever since the 1500s, when an unknown printer took a galley of type and scrambled it to make a type specimen book. It has to survived not only five centuries, but also the leap into electronic typesetting, remaining essentially unchanged. It was popularised in the 1960s with the release of Letraset sheets containing Lorem.</p>
  <div class="abs video" role="img" aria-label="Video still of laser cutting heads throwing sparks"></div>
  <div class="abs play"><svg width="44" height="44" viewBox="0 0 44 44"><path d="M17 13l13 9-13 9z" fill="#fff"/></svg></div>
</section>

<aside>
  <div class="abs quote"></div>
  <svg class="abs quote-head" width="332" height="103" viewBox="0 0 332 103"><path d="M0 0h332v72l-166 31L0 72z" fill="#0255a3"/></svg>
  <div class="abs quote-kicker">CALL US NOW FOR A</div>
  <div class="abs quote-title">FREE QUOTE</div>
  <div class="abs field" style="top:1553px">Your Name :</div>
  <div class="abs field" style="top:1610px">Email Address :</div>
  <div class="abs field" style="top:1667px">Phone no. :</div>
  <div class="abs field" style="top:1724px;height:83px">Comments :</div>
  <div class="abs btn btn-primary send">SEND A MESSAGE</div>
</aside>

<footer>
  <div class="abs footer"></div>
  <div class="abs foot-home">Home</div>
  <span class="abs foot-sep" style="left:197px">|</span>
  <span class="abs foot-link" style="left:220px">About Us</span>
  <span class="abs foot-sep" style="left:307px">|</span>
  <span class="abs foot-link" style="left:331px">Services</span>
  <span class="abs foot-sep" style="left:413px">|</span>
  <span class="abs foot-link" style="left:435px">Contact Us</span>

  <a class="abs social filled" style="left:903px" aria-label="Social link"></a>
  <a class="abs social" style="left:955px" aria-label="Social link"></a>
  <a class="abs social" style="left:1007px" aria-label="Social link"></a>
  <a class="abs social" style="left:1059px" aria-label="Social link"></a>

  <div class="abs foot-rule"></div>

  <div class="abs foot-icon" style="left:77px"><svg width="20" height="24" viewBox="0 0 20 24"><path d="M10 1a8 8 0 018 8c0 6-8 14-8 14S2 15 2 9a8 8 0 018-8z" fill="#0255a3"/><circle cx="10" cy="9" r="3" fill="#fff"/></svg></div>
  <div class="abs foot-info" style="left:131px;top:2110px">1180 W Harlow Ave #204,<br>Tempe, AZ 85281</div>

  <div class="abs foot-icon" style="left:335px"><svg width="22" height="22" viewBox="0 0 24 24"><path fill="#0255a3" d="M6.6 2.5l3 3.6-2 2.3c1.2 3 3.3 5.3 6.1 6.8l2.3-2 3.5 3.1-1.8 3.2C10.4 19.6 4.2 13 3.6 5.1z"/></svg></div>
  <div class="abs foot-info" style="left:389px;top:2123px">480.555.0182</div>

  <div class="abs foot-icon" style="left:541px"><svg width="22" height="16" viewBox="0 0 34 26"><rect x="1" y="1" width="32" height="24" rx="2" fill="#0255a3"/><path d="M2 3l15 12L32 3" stroke="#fff" stroke-width="2.5" fill="none"/></svg></div>
  <div class="abs foot-info" style="left:595px;top:2123px">hello@brightwellfinishing.com</div>

  <p class="abs copy">© <b>BRIGHTWELL FINISHING SYSTEMS</b><br>2018 . All Right Reserved</p>
</footer>
</body>
</html>
```